label for a line of bbq rubs. my competition team name is copper skillet bbq *

i already have a logo, just need a label designed for a line of bbq rubs im developing. i want the design to be clean and eye catching and my colors of my logo are black and white. these will be sold in bbq specialty stores. i have a lot of traction in the bbq competition community, they are all familiar with my logo, just need a design that will stand out and draw attention to buys online and in the stores

Target Market(s)

backyard bbq cooks

Industry/Entity Type

Food blog

Font styles to use
Sans Serif

Colors

Designer to choose only greyscale colors for use in the design.

Requirements
Must have
• project must be simple, clean, with a classic look
Nice to have
• my logo, clean and simple

i have include some examples from other companies
Should not have
• cartoons

```html
<!DOCTYPE html>
<html lang="en">
<head>
<meta charset="utf-8">
<title>Copper Skillet BBQ – Rub Labels</title>
<link rel="stylesheet" href="https://fonts.googleapis.com/css2?family=Montserrat:wght@800&family=Oswald:wght@500&display=swap">
<style>
  :root {
    --page: #e4e4e4;
    --label-black: #0b0b0b;
    --band-light: #f2f2f2;
    --band-stripe: #c9c9c9;
    --white: #ffffff;
    --chicken: #6cc03a;
    --chicken-dark: #3f8f22;
    --beef: #d8262b;
    --beef-dark: #8e1418;
    --pork: #d6489e;
    --pork-dark: #8f2a69;
  }
  * { box-sizing: border-box; margin: 0; padding: 0; }
  html, body { width: 1200px; height: 956px; overflow: hidden; }
  body {
    background: var(--page);
    display: flex;
    justify-content: center;
    align-items: center;
    gap: 48px;
  }
  .rub-label {
    width: 340px;
    height: 600px;
    background: var(--label-black);
    display: flex;
    flex-direction: column;
    align-items: center;
    box-shadow: 0 10px 30px rgba(0,0,0,0.18);
  }
  .top-band {
    width: 100%;
    height: 96px;
    background: repeating-linear-gradient(
      to bottom,
      var(--band-light) 0 7px,
      var(--band-stripe) 7px 9px
    );
  }
  .brand-name {
    margin-top: 40px;
    width: 270px;
    font-family: "Montserrat", sans-serif;
    font-weight: 800;
    font-size: 38px;
    line-height: 1.12;
    letter-spacing: 1px;
    color: var(--white);
    text-align: center;
  }
  .brand-name span { display: block; }
  .animal-mark {
    margin-top: 44px;
    width: 130px;
    height: 130px;
    border-radius: 12px;
  }
  .animal-mark.chicken { background: linear-gradient(160deg, var(--chicken), var(--chicken-dark)); }
  .animal-mark.beef { background: linear-gradient(160deg, var(--beef), var(--beef-dark)); }
  .animal-mark.pork { background: linear-gradient(160deg, var(--pork), var(--pork-dark)); }
  .flavour-tag {
    margin-top: 44px;
    width: 180px;
    height: 26px;
    background: var(--white);
    font-family: "Oswald", sans-serif;
    font-weight: 500;
    font-size: 19px;
    line-height: 26px;
    text-align: center;
    letter-spacing: 0.5px;
  }
  .flavour-tag.chicken { color: var(--chicken); }
  .flavour-tag.beef { color: var(--beef); }
  .flavour-tag.pork { color: var(--pork); }
  .footer-rule { width: 100%; height: 2px; background: var(--white); margin-top: auto; }
  .net-weight {
    font-family: "Oswald", sans-serif;
    font-weight: 500;
    font-size: 13px;
    color: var(--white);
    letter-spacing: 0.5px;
    padding: 14px 0 18px;
  }
</style>
</head>
<body>
  <section class="rub-label">
    <div class="top-band"></div>
    <h1 class="brand-name"><span>COPPER</span><span>SKILLET</span><span>BBQ</span></h1>
    <div class="animal-mark chicken" role="img" aria-label="Green rooster head illustration"></div>
    <p class="flavour-tag chicken">CHICKEN RUB</p>
    <div class="footer-rule"></div>
    <p class="net-weight">NET WEIGHT : 3 OZ ( 85G )</p>
  </section>
  <section class="rub-label">
    <div class="top-band"></div>
    <h1 class="brand-name"><span>COPPER</span><span>SKILLET</span><span>BBQ</span></h1>
    <div class="animal-mark beef" role="img" aria-label="Red cow head illustration"></div>
    <p class="flavour-tag beef">BEEF RUB</p>
    <div class="footer-rule"></div>
    <p class="net-weight">NET WEIGHT : 3 OZ ( 85G )</p>
  </section>
  <section class="rub-label">
    <div class="top-band"></div>
    <h1 class="brand-name"><span>COPPER</span><span>SKILLET</span><span>BBQ</span></h1>
    <div class="animal-mark pork" role="img" aria-label="Pink pig head illustration"></div>
    <p class="flavour-tag pork">PORK RUB</p>
    <div class="footer-rule"></div>
    <p class="net-weight">NET WEIGHT : 3 OZ ( 85G )</p>
  </section>
</body>
</html>
```